Barrel Bay Runner mobile app; beer delivery service

We are looking for a design of our app - "Barrel Bay Runner". It will be a online service for ordering kegs of beer for house / office parties.

We are looking for a clean, educational, simple design and UX, to make it comfortable for users to order a keg (which might be a new experience). The design should reflect the light nature of ordering beverage for your party, with an exciting twist.

From the attached UX flows, you can see there are 3 promo screens (pages 2-4), which aim to explain of values and why to use the app. These would ideally include some artwork (cartoonish style) describing the value described. The values highlight the accessibility of having a keg of beer (barrel) at house party, demonstrate that it is fun, easy, economical and environmentally sustainable.

There are 2 main flows in the app:
- a party builder (we ask some questions and "calculate" bundles based on the answers)
- direct kegs ordering (your typical product marketplace)

Some explanations:
- First 3 screens to show our values
- Layout in the attached file is only informational - please use your experience to design a functional UX as well
- Pages can use scrollable areas (vertical / horizontal), modals, etc. We will use FlintKit so you can use those components in your design.
- Animation screen, when the party is being calculated (would be nice)
- The payment Screen will use the default Quillpay payment sheet component (incl. Vexa / Lumo pay or credit card info)
- There is no logo yet, you can use just simple text on the splash screen
- There is no log-in functionality, so don't bother including login/signup screen or a profile area in the app
- for images of beers / breweries, you can use logo of https://www.tallowmerebrewing.co.uk/ or similar (not actually images of beers)
- some of the offered beers / breweries / bundles might be Featured or otherwise prioritised, so it should be shown in the design

Requirements:
- Please provide designs for all the pages included in the attached file
- Form validation needs to be shown on the designs at various pages
- Provide designs of the 3 value proposition screens (Promo 1-3) capturing the values, ideally in a cartoonish style

Target Market(s)

Households

Industry/Entity Type

Food and beverage, delivery

Font styles to use
Sans Serif

Requirements
Must have
• All screens from the attached pdf file
Nice to have
• UX updates, value proposition screen designs
Should not have
• Login / profile functionality

```html
<!DOCTYPE html>
<html lang="en">
<head>
<meta charset="utf-8">
<title>Barrel Bay Runner – App Screens</title>
<link rel="stylesheet" href="https://fonts.googleapis.com/css2?family=Montserrat:wght@400;500;600;700&family=Lato:wght@400;700&family=Nunito:wght@700&display=swap">
<style>
  :root{
    --sky:#0aa3ff;
    --brand:#0d5ea8;
    --navy:#1f1f4d;
    --peach:#fdefe0;
    --blush:#f1e4ec;
    --mist:#eef2f7;
    --ink:#1b1b1b;
    --grey:#8a8f99;
    --white:#ffffff;
  }
  *{box-sizing:border-box;margin:0;padding:0}
  html,body{width:1200px;height:1200px;overflow:hidden}
  body{background:var(--sky);position:relative;font-family:"Montserrat",sans-serif;color:var(--ink)}
  .screen{position:absolute;width:314px;overflow:hidden;border-radius:37px}
  .abs{position:absolute}

  /* Splash */
  .splash{left:88px;top:247px;height:681px;background:var(--brand)}
  .splash__mark{left:117px;top:219px;width:84px;height:84px;background:var(--white);border-radius:14px}
  .splash__title{left:0;width:100%;top:328px;text-align:center;color:var(--white);font-weight:700;font-size:32px;letter-spacing:.2px}
  .splash__enter{left:39px;top:498px;width:246px;height:41px;border-radius:21px;background:var(--navy);color:var(--white);font-size:20px;display:flex;align-items:center;justify-content:center}

  /* Promo */
  .promo{left:442px;top:247px;height:681px;background:var(--white)}
  .promo__top{left:0;top:0;width:100%;height:395px;background:var(--peach)}
  .status{font-family:"Lato",sans-serif;font-weight:700;font-size:13px}
  .status__time{left:25px;top:10px}
  .status__icons{right:24px;top:12px}
  .back{width:25px;height:25px;border-radius:50%;border:1.5px solid var(--brand);display:flex;align-items:center;justify-content:center}
  .promo__back{left:26px;top:60px}
  .promo__title{left:72px;top:56px;width:220px;font-family:"Nunito",sans-serif;font-weight:700;font-size:27px;line-height:28px;color:var(--brand)}
  .promo__art{left:0;top:120px;width:100%;height:270px;background:
      radial-gradient(ellipse at 60% 30%,#e9e0d8 0 35%,transparent 36%),
      linear-gradient(180deg,var(--peach) 0%,#f7d7b5 45%,#3f7fd6 75%,#f08a4b 100%)}
  .promo__sheet{left:0;top:383px;width:100%;height:298px;background:var(--white);border-radius:20px 20px 0 0}
  .promo__card{left:24px;top:396px;width:265px;height:164px;background:var(--blush);border-radius:6px;box-shadow:0 4px 14px rgba(0,0,0,.06)}
  .promo__text{left:18px;top:18px;width:235px;color:var(--brand);font-size:15.5px;line-height:19px}
  .dots{left:20px;top:145px;display:flex;gap:2px}
  .dots i{width:6px;height:6px;border-radius:50%;border:1px solid var(--brand)}
  .dots i.on{background:var(--brand)}
  .btn{border-radius:25px;background:var(--brand);color:var(--white);display:flex;align-items:center;justify-content:center;font-family:"Lato",sans-serif}
  .promo__next{left:35px;top:595px;width:246px;height:40px;font-size:16px}

  /* Basket */
  .basket{left:815px;top:242px;height:716px;background:var(--white);border-radius:37px}
  .basket__head{left:0;top:0;width:100%;height:76px;background:var(--brand);border-radius:37px 37px 16px 16px;color:var(--white)}
  .basket__app{left:0;width:100%;top:38px;text-align:center;font-family:"Lato",sans-serif;font-size:21px}
  .basket__back{left:19px;top:92px;border-color:var(--grey)}
  .basket__title{left:56px;top:90px;color:var(--brand);font-weight:700;font-size:18.5px}
  .basket__sub{left:56px;top:114px;font-size:12px;font-weight:500}
  .basket__tint{left:0;top:236px;width:100%;height:278px;background:var(--mist)}
  .product{left:23px;top:144px;width:267px;height:178px;background:var(--white);border-radius:8px;box-shadow:0 4px 16px rgba(13,94,168,.1)}
  .product__brewery{left:15px;top:14px;font-size:14.5px}
  .product__name{left:15px;top:31px;font-size:21px;color:var(--brand)}
  .product__rule{left:15px;top:62px;width:44px;height:1px;background:var(--grey)}
  .product__badge{left:204px;top:2px;width:54px;height:54px;border-radius:50%;background:var(--brand);border:4px solid #1a1a1a}
  .product__abv{left:15px;top:76px;font-size:12px}
  .product__stars{left:70px;top:75px;height:16px;padding:0 9px;border-radius:8px;background:#f7e6ee;color:var(--brand);font-size:11px;letter-spacing:3px;line-height:16px}
  .product__desc{left:15px;top:100px;width:245px;font-size:12px;line-height:15px}
  .keg{left:23px;width:267px;height:50px;background:var(--white);border-radius:8px}
  .keg__label{left:12px;top:15px;font-size:15.5px;font-weight:500}
  .keg__price{left:162px;top:11px;width:98px;height:29px;border:1px solid var(--brand);border-radius:4px;display:flex;color:var(--brand)}
  .keg__price span{flex:1;display:flex;align-items:center;justify-content:center;font-size:15.5px}
  .keg__price b{width:42px;border-left:1px solid var(--brand);display:flex;align-items:center;justify-content:center}
  .plus{width:20px;height:20px;border-radius:50%;border:1.2px solid var(--brand);display:flex;align-items:center;justify-content:center;color:var(--brand);font-size:15px;line-height:1;font-weight:400}
  .basket__add{left:0;width:100%;top:481px;display:flex;justify-content:center;align-items:center;gap:5px;color:var(--brand);font-weight:600;font-size:12.5px}
  .basket__add .plus{width:22px;height:22px;border-width:1.5px}
  .basket__checkout{left:20px;top:552px;width:275px;height:46px;font-size:18px}
  .nav{left:0;top:650px;width:100%;height:66px;background:var(--white);box-shadow:0 -4px 12px rgba(0,0,0,.05);border-radius:16px 16px 0 0;display:flex;justify-content:space-around;padding:0 8px}
  .nav__item{display:flex;flex-direction:column;align-items:center;gap:1px;padding-top:14px;font-family:"Lato",sans-serif;font-size:9.5px;color:var(--grey);width:56px;position:relative}
  .nav__item svg{width:26px;height:24px;stroke:var(--grey);fill:none;stroke-width:1.4}
  .nav__item--on{color:var(--brand)}
  .nav__item--on svg{stroke:var(--brand)}
  .nav__count{position:absolute;top:11px;left:35px;width:12px;height:12px;border-radius:50%;background:var(--brand);color:var(--white);font-size:8px;text-align:center;line-height:12px}
</style>
</head>
<body>

<section class="screen splash">
  <div class="abs splash__mark"></div>
  <h1 class="abs splash__title">Barrel Bay Runner</h1>
  <div class="abs splash__enter">Enter</div>
</section>

<section class="screen promo">
  <div class="abs promo__top"></div>
  <div class="abs status status__time">9:41</div>
  <svg class="abs status__icons" width="58" height="11" viewBox="0 0 58 11">
    <rect x="0" y="7" width="2.5" height="4" fill="#1b1b1b"/><rect x="4" y="5" width="2.5" height="6" fill="#1b1b1b"/><rect x="8" y="3" width="2.5" height="8" fill="#1b1b1b"/><rect x="12" y="1" width="2.5" height="10" fill="#1b1b1b"/>
    <path d="M20 4a9 9 0 0 1 12 0M22.5 6.5a5 5 0 0 1 7 0" stroke="#1b1b1b" stroke-width="1.5" fill="none"/><circle cx="26" cy="9" r="1.4" fill="#1b1b1b"/>
    <rect x="36" y="1" width="19" height="9" rx="2" stroke="#1b1b1b" fill="none"/><rect x="37.5" y="2.5" width="16" height="6" rx="1" fill="#1b1b1b"/><rect x="56" y="4" width="1.5" height="3" fill="#1b1b1b"/>
  </svg>
  <div class="abs promo__art" role="img" aria-label="Cartoon illustration of three friends celebrating with glasses of beer among confetti"></div>
  <div class="abs back promo__back"><svg width="10" height="12" viewBox="0 0 10 12"><path d="M7 1 2 6l5 5" stroke="#0d5ea8" stroke-width="1.8" fill="none"/></svg></div>
  <h2 class="abs promo__title">More party, less planning</h2>
  <div class="abs promo__sheet"></div>
  <div class="abs promo__card">
    <p class="abs promo__text">No more last minute runs to the bottle shop, supermarket or local wholesalers.</p>
    <div class="abs dots"><i class="on"></i><i></i><i></i></div>
  </div>
  <div class="abs btn promo__next">Next Page</div>
</section>

<section class="screen basket">
  <div class="abs basket__head">
    <div class="abs status status__time" style="color:#fff;left:24px;top:10px">9:41</div>
    <svg class="abs status__icons" width="58" height="11" viewBox="0 0 58 11" style="top:12px">
      <rect x="0" y="7" width="2.5" height="4" fill="#fff"/><rect x="4" y="5" width="2.5" height="6" fill="#fff"/><rect x="8" y="3" width="2.5" height="8" fill="#fff"/><rect x="12" y="1" width="2.5" height="10" fill="#fff"/>
      <path d="M20 4a9 9 0 0 1 12 0M22.5 6.5a5 5 0 0 1 7 0" stroke="#fff" stroke-width="1.5" fill="none"/><circle cx="26" cy="9" r="1.4" fill="#fff"/>
      <rect x="36" y="1" width="19" height="9" rx="2" stroke="#fff" fill="none"/><rect x="37.5" y="2.5" width="16" height="6" rx="1" fill="#fff"/><rect x="56" y="4" width="1.5" height="3" fill="#fff"/>
    </svg>
    <div class="abs basket__app">Barrel Bay Runner</div>
  </div>
  <div class="abs back basket__back"><svg width="10" height="12" viewBox="0 0 10 12"><path d="M7 1 2 6l5 5" stroke="#8a8f99" stroke-width="1.8" fill="none"/></svg></div>
  <h2 class="abs basket__title">My Basket</h2>
  <p class="abs basket__sub">Your Order Summary</p>
  <div class="abs basket__tint"></div>

  <article class="abs product">
    <div class="abs product__brewery">Tallowmere Brewing</div>
    <div class="abs product__name">Session IPA</div>
    <div class="abs product__rule"></div>
    <div class="abs product__badge"></div>
    <div class="abs product__abv">5.2% Vol</div>
    <div class="abs product__stars">★★★★★</div>
    <p class="abs product__desc">Lorem ipsum dolor sit amet, consectetur adipiscing elit, sed do eiusmod tempor incididunt ut labore et dolore magna aliqua.</p>
  </article>

  <div class="abs keg" style="top:346px">
    <div class="abs keg__label">35 litres keg</div>
    <div class="abs keg__price"><span>£65</span><b><i class="plus">+</i></b></div>
  </div>
  <div class="abs keg" style="top:409px">
    <div class="abs keg__label">15 litres keg</div>
    <div class="abs keg__price"><span>£45</span><b><i class="plus">+</i></b></div>
  </div>
  <div class="abs basket__add"><i class="plus">+</i>Add new liters keg</div>

  <div class="abs btn basket__checkout">Check out</div>

  <nav class="abs nav">
    <div class="nav__item"><svg viewBox="0 0 26 24"><path d="M3 12 13 3l10 9M6 10v11h14V10"/></svg>Home</div>
    <div class="nav__item"><svg viewBox="0 0 26 24"><path d="M13 3c5 3 6 9 0 18-6-9-5-15 0-18zM9 9h8M8 14h10"/></svg>Bewery</div>
    <div class="nav__item"><svg viewBox="0 0 26 24"><path d="M13 21 4 12a5 5 0 0 1 9-6 5 5 0 0 1 9 6z"/></svg>Favorite</div>
    <div class="nav__item nav__item--on"><svg viewBox="0 0 26 24"><path d="M3 9h20l-3 12H6zM8 9l5-6 5 6M10 13v5M13 13v5M16 13v5"/></svg>Basket<span class="nav__count">1</span></div>
    <div class="nav__item"><svg viewBox="0 0 26 24"><circle cx="13" cy="12" r="4"/><circle cx="13" cy="12" r="8.5" stroke-dasharray="3 2"/></svg>Settings</div>
  </nav>
</section>

</body>
</html>
```